The Bright Meadow Foundation

This is a non profit . We are a 501(c)(3) charitable organization in the United States. The organization is a volunteer based group providing basic healthcare to those living in underserved rural areas around the world. I have attached a brochure that provides some information about the organization. We are looking for a basic 5 page web page Page 1 Photos that fade into the next x 3 with mission statementPage 2 About us - details about bright meadow foundation. also introducing our Founders of the organization. Marina Kellet, M.D. Dorla Penn , FNP, Rosa Tembley, FNP, Wade Marlow. ( will provide you info on each.Page 3 Projects coming up and futurePage 4 Get involved - Give a donation, Volunteer, Corporate supportPage 5 Support us and contact us with a message box.We mainly work in South America but anticipate trave to South Africa in the near future. Colors bright with emphasis on Reds and Purples. I have attached some photos and ideas. You can use or not use ok to use something similar if you so like

Target Market(s)

People interested in volunteering time or money to overseas medical work. NOT a religious base

Coding

Coded - Design and coding required

Number of Pages Required

1 page

Colors
876aae
ec1f27
f37022
9bcb3c

Requirements
Must have
• Colorful pictures nature, brings out emotion, colorful, children from various parts of the world, animals.
• Tried to down load some pictures but would not go thru.

```html
<!DOCTYPE html>
<html lang="en">
<head>
<meta charset="utf-8">
<title>The Bright Meadow Foundation</title>
<link href="https://fonts.googleapis.com/css2?family=Montserrat:wght@400;500;600;700&display=swap" rel="stylesheet">
<style>
:root{
  --purple:#876aae;
  --purple-deep:#6f5596;
  --green:#9bcb3c;
  --ink:#1e1a22;
  --text:#3a3640;
  --card:#f1eff2;
  --dark-card:#221a2a;
  --white:#ffffff;
}
*{box-sizing:border-box;margin:0;padding:0}
html,body{width:1200px;height:3873px;overflow:hidden}
body{font-family:'Montserrat',sans-serif;color:var(--text);background:var(--white);position:relative}
.abs{position:absolute}

/* header */
.site-header{position:absolute;left:0;top:0;width:1200px;height:89px;background:var(--white)}
.brand{position:absolute;left:89px;top:30px;display:flex;align-items:center;gap:8px;font-size:14px;font-weight:600;color:var(--purple);white-space:nowrap}
.brand-dot{width:16px;height:16px;border-radius:50%;background:var(--green)}
.nav-link{position:absolute;top:36px;font-size:13px;color:#8a8790}
.nav-link.active{color:var(--purple);font-weight:600;border-bottom:2px solid var(--purple);padding-bottom:5px}
.btn-donate-top{position:absolute;left:968px;top:27px;width:143px;height:36px;border:2px solid var(--purple);border-radius:6px;color:var(--purple);font-size:13px;font-weight:600;display:flex;align-items:center;justify-content:center}

/* hero */
.hero{position:absolute;left:0;top:89px;width:1200px;height:584px;background:linear-gradient(120deg,#4d4a48 0%,#7a7068 40%,#a9968a 65%,#6b5b55 100%)}
.mission{position:absolute;left:54px;top:72px;width:544px;height:455px;background:var(--green);border:6px solid var(--purple);border-radius:180px 180px 240px 240px;color:var(--white);text-align:center;padding:80px 40px 0}
.mission h1{font-size:27px;font-weight:600;margin-bottom:14px}
.mission p{font-size:14px;line-height:21.5px;padding:0 10px}
.dots{position:absolute;left:566px;top:559px;display:flex;gap:6px;align-items:center}
.dots span{width:10px;height:10px;border-radius:50%;background:var(--white)}
.dots span.on{width:36px;border-radius:6px;background:var(--green)}

/* about + projects backdrop */
.backdrop{position:absolute;left:0;top:673px;width:1200px;height:1520px;background:
 radial-gradient(ellipse 300px 260px at 230px 160px,rgba(243,183,120,.28),transparent),
 radial-gradient(ellipse 260px 240px at 850px 120px,rgba(236,100,90,.22),transparent),
 radial-gradient(ellipse 520px 420px at 600px 900px,rgba(120,190,230,.28),transparent),
 radial-gradient(ellipse 300px 300px at 80px 1200px,rgba(240,150,180,.25),transparent),
 radial-gradient(ellipse 320px 300px at 1100px 1300px,rgba(150,200,230,.25),transparent),
 #fbfbfd}
.section-title{position:absolute;font-size:25px;font-weight:600;color:var(--ink)}
.about-text{position:absolute;left:93px;top:817px;width:1018px;font-size:14px;line-height:21.5px;color:var(--text)}
.link-more{position:absolute;font-size:17px;font-weight:600;color:var(--purple);text-decoration:underline;display:flex;align-items:center;gap:8px}

.team-card{position:absolute;top:1070px;width:248px;height:192px;background:var(--purple);border-radius:6px;text-align:center;color:var(--white);box-shadow:0 2px 6px rgba(0,0,0,.15)}
.team-card .avatar{position:absolute;left:87px;top:23px;width:75px;height:75px;border-radius:50%;background:linear-gradient(135deg,#c9a78c,#7a5b4a);border:3px solid #e9e2f1}
.team-card .name{position:absolute;left:0;right:0;top:115px;font-size:19px;font-weight:600;color:var(--green)}
.team-card .role{position:absolute;left:0;right:0;top:155px;font-size:16px;font-weight:600}
.team-card.intro{background:var(--dark-card)}
.socials{position:absolute;left:20px;right:20px;top:42px;display:flex;justify-content:space-around}
.socials span{width:30px;height:30px;border-radius:50%;border:2px solid #d8d2e0}
.team-card.intro p{position:absolute;left:30px;right:30px;top:102px;font-size:14px;line-height:20px}

.projects-intro{position:absolute;left:170px;top:1460px;width:860px;text-align:center;font-size:14px;line-height:21px}
.project{position:absolute;top:1552px;width:336px;height:489px;background:var(--card);border-radius:6px}
.project .photo{height:193px;border-radius:6px 6px 0 0}
.project .figures{position:absolute;left:18px;right:18px;top:208px;display:flex;justify-content:space-between;font-size:15px;font-weight:600;color:var(--ink)}
.project .figures b{color:var(--purple);font-weight:500}
.project .bar{position:absolute;left:18px;right:18px;top:238px;height:10px;border-radius:5px;background:#dedbe2;overflow:hidden}
.project .bar i{display:block;height:100%;background:var(--purple);border-radius:5px}
.project .pct{position:absolute;left:0;right:0;top:266px;text-align:center;font-size:14px;color:var(--purple)}
.project h3{position:absolute;left:0;right:0;top:298px;text-align:center;font-size:25px;font-weight:600;color:var(--ink)}
.project p{position:absolute;left:20px;right:20px;top:336px;text-align:center;font-size:14px;line-height:22px}
.project .btn{position:absolute;left:96px;top:471px;width:143px;height:36px;border-radius:6px;background:var(--purple);color:var(--white);font-size:13px;font-weight:500;display:flex;align-items:center;justify-content:center;box-shadow:0 2px 4px rgba(0,0,0,.2)}

/* impact band */
.impact{position:absolute;left:0;top:2193px;width:1200px;height:384px;background:var(--purple)}
.impact h2{position:absolute;left:88px;top:106px;width:380px;font-size:25px;line-height:32px;font-weight:600;color:var(--white)}
.btn-join{position:absolute;left:88px;top:268px;width:144px;height:36px;background:var(--white);border:3px solid var(--green);border-radius:6px;color:var(--purple);font-size:13px;font-weight:600;display:flex;align-items:center;justify-content:center}
.stat{position:absolute;top:90px;width:240px;text-align:center;color:var(--white)}
.stat .icon{width:157px;height:157px;border-radius:50%;margin:0 auto;background:radial-gradient(circle,#a9d35a 0%,var(--green) 70%);border:3px solid #e8f3d0}
.stat .num{margin-top:14px;font-size:14px;color:var(--green);font-weight:600}
.stat .label{margin-top:4px;font-size:18px;font-weight:600}

/* contact */
.contact{position:absolute;left:0;top:2577px;width:1200px;height:857px;background:linear-gradient(135deg,#3f5f5c 0%,#5b6e62 35%,#8a7560 60%,#6a5a4c 80%,#3d4a45 100%)}
.contact h2{position:absolute;left:88px;top:175px;font-size:50px;font-weight:700;color:var(--green);letter-spacing:1px}
.contact .tag{position:absolute;left:88px;top:270px;font-size:30px;line-height:40px;font-weight:700;color:var(--white)}
.contact .tag em{font-style:normal;color:var(--green)}
.field{position:absolute;left:702px;width:409px;background:var(--white);border:3px solid var(--green);border-radius:4px;padding:15px;font-family:'Montserrat',sans-serif;font-size:17px;color:#b6b3ba}
.btn-send{position:absolute;left:860px;top:681px;width:251px;height:37px;background:var(--green);border-radius:5px;color:var(--white);font-size:18px;font-weight:600;display:flex;align-items:center;justify-content:center}

/* footer */
.footer{position:absolute;left:0;top:3434px;width:1200px;height:357px;background:var(--white)}
.contact-line{position:absolute;left:93px;display:flex;align-items:flex-start;gap:12px;font-size:18px;font-weight:500;color:var(--purple);line-height:26px}
.contact-line .ic{width:30px;height:30px;border-radius:50%;background:#f0eef3;display:flex;align-items:center;justify-content:center;flex:none}
.footer-socials span{position:absolute;top:256px;width:54px;height:54px;border-radius:50%;background:var(--white);box-shadow:0 2px 8px rgba(0,0,0,.15)}
.foot-col{position:absolute;top:62px}
.foot-col h4{font-size:22px;font-weight:600;margin-bottom:20px}
.foot-col li{list-style:none;font-size:18px;color:var(--ink);height:37.5px}
.foot-col.green h4{color:var(--green)}
.foot-col.violet h4{color:var(--purple)}
.copyright{position:absolute;left:0;top:3791px;width:1200px;height:82px;background:var(--purple);display:flex;align-items:center;justify-content:center;font-size:11px;color:var(--green)}
</style>
</head>
<body>

<header class="site-header">
  <div class="brand"><span class="brand-dot"></span>Bright Meadow Foundation</div>
  <span class="nav-link active" style="left:334px">Home</span>
  <span class="nav-link" style="left:425px">About Us</span>
  <span class="nav-link" style="left:541px">Projects</span>
  <span class="nav-link" style="left:648px">Get Involved</span>
  <span class="nav-link" style="left:788px">Contact Us</span>
  <span class="btn-donate-top">Donate</span>
</header>

<section class="hero" role="img" aria-label="Photo of smiling schoolchildren in uniforms running down a village street">
  <div class="mission">
    <h1>Mission Statement</h1>
    <p>Aliquam faucibus, odio nec commodo aliquam, nequ felis placerat dui, a porta ante lectus dapibus est. Aliquam abibendum mi, sed condimentum est. Mauris arcu odio, Aliquam faucibus, odio nec commodo aliquam, vestibulum quis dapibus sit amet, finibus id tur pis. Aliquam semper fringilla semper. Sed nec velit sit amet dolor pulvina feugiat interdum egestas, nibh ex maxi mus arcu, non posuere sem nulla in augue.</p>
  </div>
  <div class="dots"><span class="on"></span><span></span><span></span></div>
</section>

<div class="backdrop" role="img" aria-label="Faint background of colourful painted hands"></div>

<h2 class="section-title" style="left:88px;top:773px">About Us</h2>
<p class="about-text">Aliquam faucibus, odio nec commodo aliquam, neque felis placerat dui, a port ante lectus dapibus est. Aliquam a bibendum mi, sed condimentum est. Mauris arcu odio, vestibulum quis dapibus sit amet, finibus id turpis. Aliquam semper fringilla semper. Sed nec velit sit amet dolor pulvinar feugiat. Suspendisse blandit, nulla sed interdum egestas, nibh ex maximus arcu, non posuere sem nulla in augue. Class aptent taciti sociosqu ad litora torquent per conubia nostra, per inceptos himenaeos. Maecenas mattis sapien vel sollicitudin blandit. Donec nec porttitor eros. Praesent blandit, erat non vehicula rutrum, mauris orci scelerisque urna, rutrum malesuada odio magna at felis. Fusce convallis elit in risus tincidunt ullamcorper. Aliquam maximus dolor turpis, nec commodo libero mattis</p>
<span class="link-more" style="left:970px;top:988px">Read More
  <svg width="12" height="12" viewBox="0 0 12 12"><path d="M2 2l4 4 4-4M2 6l4 4 4-4" fill="none" stroke="#876aae" stroke-width="1.6"/></svg></span>

<h2 class="section-title" style="left:88px;top:1021px">Our Team</h2>
<div class="team-card intro" style="left:88px">
  <div class="socials"><span></span><span></span><span></span><span></span></div>
  <p>Cras eu elit congue, placerat dui ut, tincidunt nisl. Nulla leo elit,</p>
</div>
<div class="team-card" style="left:346px">
  <div class="avatar" role="img" aria-label="Portrait of Rosa Tembley"></div>
  <div class="name">Rosa Tembley</div><div class="role">FNP</div>
</div>
<div class="team-card" style="left:605px">
  <div class="avatar" role="img" aria-label="Portrait of Dorla Penn" style="background:linear-gradient(135deg,#b8242a,#5a1f1f)"></div>
  <div class="name">Dorla Penn</div><div class="role">FNP</div>
</div>
<div class="team-card" style="left:864px">
  <div class="avatar" role="img" aria-label="Portrait of Wade Marlow" style="background:linear-gradient(135deg,#6a4bd0,#2a2a6a)"></div>
  <div class="name">Wade Marlow</div><div class="role">FNP</div>
</div>

<h2 class="section-title" style="left:0;width:1200px;text-align:center;top:1418px">Projects</h2>
<p class="projects-intro">Duis pretium gravida enim, vel maximus ligula fermentum a. Sed rhoncus eget ex id egestas. Nam nec nisl placerat, tempus erat a, condimentum metus. Curabitur nulla nisi, lacinia at lobortis at, suscipit at nibh. Proin quis lectus finibus, mollis purus vitae, rutrum neque. Pellentesque habitant morbi tristique senectus</p>

<article class="project" style="left:88px">
  <div class="photo" role="img" aria-label="Black and white photo of a young child" style="background:linear-gradient(135deg,#d8d8d8,#6a6a6a)"></div>
  <div class="figures"><span>Raised: <b>$9000</b></span><span>Goal: <b>$10000</b></span></div>
  <div class="bar"><i style="width:50%"></i></div>
  <div class="pct">50%</div>
  <h3>Child Education</h3>
  <p>Duis pretium gravida enim, vel maximus ligula fermentum a. Sed rhoncus eget ex id egestas. Nam nec nisl placerat, tempus erat a, condimentum metus. Curabitur nulla</p>
  <span class="btn">Donate Now</span>
</article>
<article class="project" style="left:432px">
  <div class="photo" role="img" aria-label="Photo of a smiling child leaning on a red boat among green trees" style="background:linear-gradient(180deg,#7fa04a 0%,#4f7a3a 55%,#a83a32 75%,#3a6a8a 100%)"></div>
  <div class="figures"><span>Raised: <b>$9000</b></span><span>Goal: <b>$10000</b></span></div>
  <div class="bar"><i style="width:25%"></i></div>
  <div class="pct">25%</div>
  <h3>Child Education</h3>
  <p>Duis pretium gravida enim, vel maximus ligula fermentum a. Sed rhoncus eget ex id egestas. Nam nec nisl placerat, tempus erat a, condimentum metus. Curabitur nulla</p>
  <span class="btn">Donate Now</span>
</article>
<article class="project" style="left:777px">
  <div class="photo" role="img" aria-label="Photo of a mother holding her child in a wooden home" style="background:linear-gradient(135deg,#6a5a4a,#2e2620 60%,#8a3a3a)"></div>
  <div class="figures"><span>Raised: <b>$5000</b></span><span>Goal: <b>$10000</b></span></div>
  <div class="bar"><i style="width:92%"></i></div>
  <div class="pct">90%</div>
  <h3>Child Education</h3>
  <p>Duis pretium gravida enim, vel maximus ligula fermentum a. Sed rhoncus eget ex id egestas. Nam nec nisl placerat, tempus erat a, condimentum metus. Curabitur nulla</p>
  <span class="btn">Donate Now</span>
</article>
<span class="link-more" style="left:497px;top:2080px">Show more Projects
  <svg width="12" height="12" viewBox="0 0 12 12"><path d="M2 2l4 4 4-4M2 6l4 4 4-4" fill="none" stroke="#876aae" stroke-width="1.6"/></svg></span>

<section class="impact">
  <h2>We are serving humanity since 25 years to people with trust and we are happy.</h2>
  <span class="btn-join">Join Us</span>
  <div class="stat" style="left:477px">
    <div class="icon" role="img" aria-label="Illustration of a hand holding a heart"></div>
    <div class="num">$99,952</div><div class="label">Donations</div>
  </div>
  <div class="stat" style="left:696px">
    <div class="icon" role="img" aria-label="Illustration of a group of volunteers"></div>
    <div class="num">952</div><div class="label">Volunteers</div>
  </div>
  <div class="stat" style="left:921px">
    <div class="icon" role="img" aria-label="Illustration of hands sheltering a family"></div>
    <div class="num">24hrs</div><div class="label">Corporate Support</div>
  </div>
</section>

<section class="contact" role="img" aria-label="Photo of a young girl looking through a chain-link fence">
  <h2>CONTACT US</h2>
  <p class="tag">They <em>NEED</em><br>your help....</p>
  <div class="field" style="top:173px;height:58px">Enter Your Name</div>
  <div class="field" style="top:250px;height:58px">Enter Your Email</div>
  <div class="field" style="top:325px;height:334px">Enter Your Message</div>
  <span class="btn-send">Send</span>
</section>

<footer class="footer">
  <div class="brand" style="top:62px;left:93px"><span class="brand-dot"></span>Bright Meadow Foundation</div>
  <div class="contact-line" style="top:122px">
    <span class="ic"><svg width="14" height="14" viewBox="0 0 24 24"><path d="M6.6 10.8a15 15 0 006.6 6.6l2.2-2.2a1 1 0 011-.25 11.4 11.4 0 003.6.57 1 1 0 011 1V20a1 1 0 01-1 1A17 17 0 013 4a1 1 0 011-1h3.5a1 1 0 011 1c0 1.25.2 2.45.57 3.6a1 1 0 01-.25 1z" fill="#8a8790"/></svg></span>(555)310-7724</div>
  <div class="contact-line" style="top:170px">
    <span class="ic"><svg width="14" height="14" viewBox="0 0 24 24"><path d="M12 2a7 7 0 00-7 7c0 5.2 7 13 7 13s7-7.8 7-13a7 7 0 00-7-7zm0 9.5A2.5 2.5 0 1112 6.5a2.5 2.5 0 010 5z" fill="#8a8790"/></svg></span>18 Linden Row, 4th Floor<br>Riverton, Malawi</div>
  <div class="footer-socials"><span style="left:87px"></span><span style="left:150px"></span><span style="left:212px"></span><span style="left:275px"></span></div>
  <div class="foot-col green" style="left:432px"><h4>Get Involved</h4><ul><li>Donate</li><li>Account</li><li>Employer Center</li><li>Projects</li><li>Projects</li></ul></div>
  <div class="foot-col violet" style="left:682px"><h4>Community</h4><ul><li>Help/Contact Us</li><li>About Us</li><li>Blog</li><li>Guides</li><li>Guides</li></ul></div>
  <div class="foot-col violet" style="left:938px"><h4>Work With Us</h4><ul><li>Research</li><li>Location</li><li>Advertisers</li><li>Careers</li><li>Careers</li></ul></div>
</footer>
<div class="copyright">Copyrights ©2019 -BRIGHT MEADOW FOUNDATION</div>

</body>
</html>
```